Wordpress Design and Coding for New Residential and Commercial Lawn and Landscape Co.

I need a Wordpress site with coding built for a startup Residential and Commercial Lawn and Landscape Company. I'm uploading our business card and logo files. I'd like a really clean design, with icons to describe services and who we serve. We don't have a lot of content being new.
We offer a large variety of services. Our 2 target customers would be residential and commercial. We offer the following services: Lawn Care and Mowing, Hedge and Shrub Trimming, Removal and Clean Up, Aeration and Sod, Mulch and Rock Installation, Landscape Installations and Renovations, and Commercial Snow Removal in the winter for Retail Shopping Centers, Communities, and other larger customers.
We serve Baltimore County, Harford County, and Surrounding areas.
Target Market(s)
We have 2 main types of customer.
1. Residential - this includes lawn maintenance, plantings, mulch & rock installs, and maintenance, etc.
2. Commercial - this includes complete care from design, planting, maintenance, etc. Communities, Property Managers, Housing Associations, Shopping Centers, Retail, etc.
Industry/Entity Type
Landscape
Coding
Coded - Design and coding required
Requirements
Must have
- Clean design. Nice distinct icons to display services and other information. Large Bold eye popping landscape photo at top.
- I've included screen shots of designs I like. Please do not copy them, they are competitors.
Nice to have
- 1. Link to our Facebook page - fb.com/brightfurrowmd
- 2. Link to FB Photos for Gallery Section - https://www.example-social.com/pg/BrightFurrowMD/photos/
- 3. Why Choose Us section.
- 4. Contact form that includes 4 sections - Name, Phone #, Service Address, and Comments.
- 5. Reviews/Testimonials on Landing Page

```html
<!DOCTYPE html>
<html lang="en">
<head>
<meta charset="utf-8">
<title>Bright Furrow Lawn &amp; Landscape</title>
<link rel="stylesheet" href="https://fonts.googleapis.com/css2?family=Montserrat:wght@500;600;700&family=Open+Sans:wght@300;400;600&family=Roboto:wght@500;700&display=swap">
<style>
:root{
  --backdrop:#e4e4e4;
  --navy:#152433;
  --slate:#2b3440;
  --footer:#272d36;
  --green:#8dc21f;
  --yellow:#f2d500;
  --blue:#1a73c4;
  --ink:#222;
  --muted:#777;
  --tile:#f7f7f7;
  --white:#fff;
}
*{box-sizing:border-box;margin:0;padding:0}
html,body{width:960px;height:1200px;overflow:hidden;background:var(--backdrop)}
body{font-family:"Open Sans",sans-serif;color:var(--ink)}
.stage{position:relative;width:1200px;height:1500px;transform:scale(.8);transform-origin:0 0;
  background:radial-gradient(ellipse at center,#f4f4f4 0%,#dcdcdc 80%)}
.page{position:absolute;left:264px;top:0;width:636px;height:1500px;background:var(--white);overflow:hidden}
.abs{position:absolute}
a{color:inherit;text-decoration:none}

/* top */
.top{left:0;top:0;width:636px;height:550px;background:var(--navy)}
.header{left:60px;top:18px;width:528px;height:39px;background:var(--white);display:flex;align-items:center;padding:0 10px}
.brand{display:flex;align-items:center;gap:8px;font-family:"Montserrat",sans-serif;font-weight:600;color:var(--green);line-height:1}
.brand-dot{width:22px;height:22px;border-radius:50%;border:3px solid var(--green)}
.brand-name{font-size:15px}
.brand-sub{font-size:7.5px;letter-spacing:2px;margin-top:3px}
.nav{margin-left:auto;display:flex;gap:21px;font-family:"Roboto",sans-serif;font-weight:500;font-size:6px;color:#333;align-items:center;height:39px}
.nav a{position:relative;height:39px;display:flex;align-items:center}
.nav .active::after{content:"";position:absolute;left:-6px;right:-6px;bottom:0;height:3px;background:var(--green)}
.search{width:15px;height:15px;border-radius:50%;background:var(--blue);display:flex;align-items:center;justify-content:center}
.hero{left:60px;top:57px;width:528px;height:238px;background:linear-gradient(135deg,#9aa0a8 0%,#8a8f97 45%,#7b7f84 70%,#5d5f5e 100%)}
.hero h1{left:32px;top:28px;font-family:"Montserrat",sans-serif;font-weight:700;font-size:29px;line-height:35px;color:var(--white)}
.hero p{left:32px;top:108px;width:330px;font-weight:300;font-size:12.5px;line-height:18px;color:var(--white)}
.chips{left:31px;top:160px;display:flex;gap:6px}
.chip{height:28px;background:var(--yellow);color:#2c5a1a;font-family:"Roboto",sans-serif;font-weight:500;font-size:7.5px;line-height:9px;text-align:center;display:flex;align-items:center;justify-content:center}

.card{top:295px;width:167px;height:185px;background:var(--white)}
.card-photo{width:167px;height:100px}
.card-tag{position:absolute;right:0;top:84px;height:16px;display:flex;font-family:"Roboto",sans-serif;font-weight:500;font-size:5.5px;color:var(--white)}
.card-tag span{background:#1b2430;padding:0 10px;display:flex;align-items:center}
.card-tag i{width:14px;background:#1b2430;display:flex;align-items:center;justify-content:center;font-style:normal;border-left:1px solid #3a4450}
.card-tag.blue span,.card-tag.blue i{background:var(--blue)}
.rule{width:14px;height:2px;background:var(--green)}
.card .rule{margin:14px 0 0 13px}
.card h3{margin:5px 13px 0;font-family:"Roboto",sans-serif;font-weight:700;font-size:8px;color:#222}
.card p{margin:8px 13px 0;font-size:5.5px;line-height:9px;color:#666}
.btn-green{left:275px;top:504px;width:100px;height:22px;border-radius:11px;background:var(--green);color:var(--white);font-family:"Roboto",sans-serif;font-weight:500;font-size:5.5px;display:flex;align-items:center;justify-content:center}

/* offer */
.offer-title{left:0;top:578px;width:636px;text-align:center;font-family:"Montserrat",sans-serif;font-weight:600;font-size:13.5px}
.offer-sub{left:0;top:597px;width:636px;text-align:center;font-size:5px;color:#888}
.offer-rule{left:311px;top:608px;width:14px;height:2px;background:var(--green)}
.tile{width:257px;height:85px;background:var(--tile);display:flex;padding:17px 15px 0 22px;gap:14px}
.tile svg{flex:none;margin-top:8px}
.tile h4{font-weight:400;font-size:8px;color:#222}
.tile p{margin-top:7px;font-size:5.5px;line-height:9.2px;color:#777}

/* services band */
.band{left:0;top:844px;width:318px;height:252px;background:var(--slate);color:var(--white)}
.band .rule{position:absolute;left:60px;top:33px}
.band h2{position:absolute;left:60px;top:38px;font-family:"Roboto",sans-serif;font-weight:700;font-size:9.5px}
.band p{position:absolute;left:60px;top:59px;width:256px;font-size:5.5px;line-height:9.2px;color:#d5d9de}
.svc{position:absolute;left:60px;display:flex;align-items:center;gap:12px;font-size:7.5px;font-weight:400}
.svc svg{flex:none}
.lawn-photo{left:318px;top:844px;width:318px;height:252px;background:linear-gradient(180deg,#b6cbe0 0%,#d7e2ea 30%,#b9b38e 48%,#6f8a3f 62%,#4d8a1f 100%)}

/* bottom columns */
.col-title{top:1131px;font-family:"Roboto",sans-serif;font-weight:700;font-size:10px;color:#222}
.col-rule{top:1127px;width:14px;height:2px;background:var(--yellow)}
.news{left:60px;width:167px}
.news-item{position:absolute;left:0;width:167px;height:46px}
.news-photo{position:absolute;left:0;top:0;width:45px;height:45px;background:linear-gradient(160deg,#5fa12e,#3f7d1d 60%,#8b2a22)}
.news-date{position:absolute;left:55px;top:2px;font-size:5px;color:#888}
.news-date::before{content:"";display:inline-block;width:5px;height:5px;background:var(--yellow);margin-right:4px;vertical-align:-1px}
.news h5{position:absolute;left:55px;top:10px;width:110px;font-weight:400;font-size:8px;line-height:11.5px;color:#222}
.more{position:absolute;right:0;font-family:"Roboto",sans-serif;font-weight:700;font-size:5.5px;color:var(--blue)}
.quote{left:241px;top:1156px;width:167px;height:120px;background:#fafafa;text-align:center}
.quote p{margin:22px 22px 0;font-style:italic;font-size:5.5px;line-height:10px;color:#888}
.quote .mark{width:14px;height:2px;background:var(--yellow);margin:6px auto 0}
.quote b{display:block;margin-top:10px;font-family:"Roboto",sans-serif;font-size:5.5px;line-height:10px;color:#222}
.arrow-btn{width:16px;height:16px;display:flex;align-items:center;justify-content:center}
.map{left:421px;top:1156px;width:167px;height:61px;background:linear-gradient(135deg,#e6ebe0,#d3dce4 60%,#a9c3de)}

/* footer */
.footer{left:0;top:1312px;width:636px;height:188px;background:var(--footer);color:#c7ccd3}
.footer h6{position:absolute;top:31px;font-family:"Roboto",sans-serif;font-weight:500;font-size:6.5px;color:var(--white);letter-spacing:.2px}
.footer ul{position:absolute;top:51px;list-style:none;font-size:5.5px;line-height:11.3px}
.footer li::before{content:"›";margin-right:5px;color:#fff}
.footer .txt{position:absolute;font-size:5.5px;line-height:9.5px}
.subscribe{position:absolute;left:60px;top:96px;width:121px;height:18px;display:flex}
.subscribe span{flex:1;background:#3a4250;font-style:italic;font-size:5.5px;padding-left:7px;display:flex;align-items:center;color:#9aa1ab}
.subscribe i{width:17px;background:var(--blue)}
.social{position:absolute;top:113px;display:flex;gap:3px}
.social span{width:12px;height:12px;border:1px solid #5a616c;background:#3a4250}
.copyright{position:absolute;left:60px;right:48px;top:160px;border-top:1px solid #3a414b;padding-top:10px;font-size:5px;color:#aeb4bc}
</style>
</head>
<body>
<div class="stage">
<div class="page">

  <section class="abs top">
    <header class="abs header">
      <div class="brand"><span class="brand-dot"></span><div><div class="brand-name">Bright Furrow</div><div class="brand-sub">LAWN &amp; LANDSCAPE</div></div></div>
      <nav class="nav">
        <a class="active" href="#">HOME</a><a href="#">ABOUT US</a><a href="#">SERVICES</a><a href="#">NEWS</a><a href="#">LOCATIONS</a><a href="#">CONTACT</a>
        <span class="search"><svg width="7" height="7" viewBox="0 0 10 10"><circle cx="4" cy="4" r="3" fill="none" stroke="#fff" stroke-width="1.5"/><line x1="6.3" y1="6.3" x2="9" y2="9" stroke="#fff" stroke-width="1.5"/></svg></span>
      </nav>
    </header>

    <div class="abs hero" role="img" aria-label="Photo of two crew members in hard hats and high-visibility jackets reviewing plans in falling snow, with a snow plough behind them">
      <h1 class="abs">Ice? Snow? Blizzard?<br>Bring it on!</h1>
      <p class="abs">In addition to creating beautiful landscapes, we manage them – through any season.</p>
      <div class="abs chips">
        <a class="chip" style="width:87px" href="#">COMMERCIAL &amp;<br>INDUSTRIAL</a>
        <a class="chip" style="width:83px" href="#">RESIDENTIAL<br>COMMUNITIES</a>
        <a class="chip" style="width:82px" href="#">RETAIL &amp;<br>RESORT</a>
      </div>
    </div>

    <article class="abs card" style="left:60px">
      <div class="card-photo" role="img" aria-label="Photo of two business people reviewing a landscape plan" style="background:linear-gradient(135deg,#d8dde2,#7f8a92 50%,#4d6b3a)"></div>
      <a class="card-tag blue" href="#"><span>READ MORE</span><i>›</i></a>
      <div class="rule"></div>
      <h3>LANDSCAPE MANAGEMENT</h3>
      <p>We have a wide experience in overland industry specific lawn solutions like seasonal planting, mulching, retail and community grounds by crew or by contract.</p>
    </article>
    <article class="abs card" style="left:240px">
      <div class="card-photo" role="img" aria-label="Photo of indoor palms and flowering plants in a building lobby" style="background:linear-gradient(180deg,#d9dcd8,#9aa59a 50%,#4f7a35 75%,#8a3f6a)"></div>
      <a class="card-tag" href="#"><span>READ MORE</span><i>›</i></a>
      <div class="rule"></div>
      <h3>INTERIOR PLANTSCAPING</h3>
      <p>We bring your plants safely to offices and lobbies across the region with our careful crews. We offer design and care visits that are fast and effective with no delays.</p>
    </article>
    <article class="abs card" style="left:421px">
      <div class="card-photo" role="img" aria-label="Photo of a yellow loader clearing snow from a parking lot" style="background:linear-gradient(180deg,#c7ccd2,#a7adb3 45%,#e9ecef 75%,#c9c9c2)"></div>
      <a class="card-tag" href="#"><span>READ MORE</span><i>›</i></a>
      <div class="rule"></div>
      <h3>SNOW &amp; ICE REMOVAL</h3>
      <p>We provide full supply of plough and salt management package including cost effective and fast lot clearing. You can also combine this package with other means of upkeep.</p>
    </article>

    <a class="abs btn-green" href="#">VIEW DETAILS</a>
  </section>

  <section>
    <h2 class="abs offer-title">What we Offer</h2>
    <div class="abs offer-sub">Residential and Commercial Lawn and Landscap</div>
    <div class="abs offer-rule"></div>

    <div class="abs tile" style="left:60px;top:628px">
      <svg width="34" height="34" viewBox="0 0 34 34"><rect x="5" y="5" width="18" height="24" fill="none" stroke="#333" stroke-width="2"/><rect x="10" y="2" width="8" height="5" fill="#333"/><line x1="9" y1="13" x2="19" y2="13" stroke="#333" stroke-width="2"/><line x1="9" y1="18" x2="19" y2="18" stroke="#333" stroke-width="2"/><line x1="9" y1="23" x2="15" y2="23" stroke="#333" stroke-width="2"/><circle cx="25" cy="22" r="6" fill="#f2b600"/><path d="M22 22l2 2 4-4" stroke="#fff" stroke-width="1.6" fill="none"/></svg>
      <div><h4>Landscape Management</h4><p>Cozy sphinx waves quart jug of bad milk. A very bad quack might jinx zippy fowls. Few quips galvanized the mock jury box. Quick brown dogs jump over the lazy fox. The jay, pig, fox, zebra, and my wolves quack!</p></div>
    </div>
    <div class="abs tile" style="left:331px;top:628px">
      <svg width="40" height="34" viewBox="0 0 40 34"><circle cx="14" cy="17" r="12" fill="none" stroke="#333" stroke-width="2"/><path d="M2 17h24M14 5c-5 6-5 18 0 24M14 5c5 6 5 18 0 24" stroke="#333" stroke-width="1.6" fill="none"/><path d="M18 18l20-4-2 3-6 1 3 9-3 1-5-8-6 1z" fill="#f2b600"/></svg>
      <div><h4>Interior Plantscaping</h4><p>To an English person, it will seem like simplified English, as a skeptical Cambridge friend of mine told me what Occidental is. The European languages are members of the same family.</p></div>
    </div>
    <div class="abs tile" style="left:60px;top:727px">
      <svg width="44" height="34" viewBox="0 0 44 34"><path d="M3 26V14l5-9h9v21z" fill="none" stroke="#333" stroke-width="2"/><rect x="17" y="16" width="12" height="10" fill="#f2b600"/><line x1="32" y1="4" x2="32" y2="28" stroke="#333" stroke-width="2"/><line x1="32" y1="28" x2="42" y2="28" stroke="#333" stroke-width="2"/><rect x="33" y="18" width="8" height="7" fill="#f2b600"/><circle cx="8" cy="28" r="3.5" fill="#333"/><circle cx="24" cy="28" r="3.5" fill="#333"/></svg>
      <div><h4>Snow &amp; Ice Removal</h4><p>The jay, pig, fox, zebra, and my wolves quack! Blowzy red vixens fight for a quick jump. Jonah Pike was gazed by a radio host for luck. A wizard's job is to vex chumps quickly in fog. Watch "Quiz Corner", Sam Treble's fun TV quiz game.</p></div>
    </div>
    <div class="abs tile" style="left:331px;top:727px">
      <svg width="40" height="34" viewBox="0 0 40 34"><rect x="3" y="4" width="24" height="17" rx="1" fill="none" stroke="#333" stroke-width="2"/><line x1="15" y1="21" x2="15" y2="27" stroke="#333" stroke-width="2"/><line x1="9" y1="27" x2="20" y2="27" stroke="#333" stroke-width="2"/><path d="M24 14v-4a2 2 0 014 0v8h2a4 4 0 014 4v6c0 3-2 5-5 5h-3c-3 0-5-2-6-5l-2-5c0-2 3-2 4 0z" fill="#f2b600"/></svg>
      <div><h4>Other Services</h4><p>The Big Oxmox advised her not to do so, because there were thousands of bad Commas, wild Question Marks and devious Semikoli, but the Little Blind Text didn't listen. She packed her seven versalia.</p></div>
    </div>
  </section>

  <section class="abs band">
    <div class="rule"></div>
    <h2>RESIDENTIAL AND COMMERCIAL LAWN AND LANDSCAPE</h2>
    <p>Lawn Care and Mowing, Hedge and Shrub Trimming, Removal and Clean Up, Aeration and Sod, Mulch and Rock Installation, Landscape Installations and Renovations, and Commercial Snow Removal</p>
    <div class="svc" style="top:104px"><svg width="28" height="18" viewBox="0 0 28 18"><path d="M14 1l7 4-7 4-7-4z" fill="#f2b600"/><path d="M7 8l7 4 7-4M7 12l7 4 7-4" stroke="#fff" stroke-width="1.6" fill="none"/></svg>Landscape Management</div>
    <div class="svc" style="top:130px"><svg width="28" height="20" viewBox="0 0 28 20"><rect x="8" y="3" width="12" height="16" rx="1" fill="#fff"/><rect x="11" y="1" width="6" height="4" fill="#fff"/><circle cx="14" cy="12" r="3.5" fill="#2b3440"/></svg>Interior Plantscaping</div>
    <div class="svc" style="top:157px"><svg width="28" height="20" viewBox="0 0 28 20"><rect x="5" y="5" width="5" height="13" fill="#fff"/><rect x="6" y="2" width="3" height="3" fill="#fff"/><rect x="12" y="7" width="11" height="11" rx="3" fill="#f2b600"/><line x1="12" y1="12" x2="23" y2="12" stroke="#2b3440" stroke-width="1.5"/></svg>Snow &amp; Ice Removal</div>
    <div class="svc" style="top:184px"><svg width="28" height="20" viewBox="0 0 28 20"><path d="M8 19V8l6-6 6 6v11h-3v-8h-6v8z" fill="none" stroke="#fff" stroke-width="1.6"/><rect x="12" y="12" width="4" height="7" fill="#f2b600"/></svg>Retail Goods</div>
    <div class="svc" style="top:213px"><svg width="28" height="20" viewBox="0 0 28 20"><rect x="1" y="5" width="12" height="9" fill="#fff"/><path d="M14 14V6c4 0 12 0 12 8z" fill="#f2b600"/><circle cx="5" cy="16" r="2.5" fill="#fff"/><circle cx="20" cy="16" r="2.5" fill="#fff"/></svg>Energy, Oil and Gas</div>
  </section>
  <div class="abs lawn-photo" role="img" aria-label="Photo of a large two-storey family home behind a freshly mowed green lawn under a cloudy sky"></div>

  <section>
    <div class="abs col-rule" style="left:60px"></div>
    <h3 class="abs col-title" style="left:60px">COMPANY NEWS</h3>
    <div class="abs news" style="top:1156px;height:120px">
      <div class="news-item" style="top:0">
        <div class="news-photo" role="img" aria-label="Photo of a red ride-on mower on a striped lawn"></div>
        <div class="news-date">APRIL 22, 2015</div>
        <h5>New service available: end-to-end lawn care</h5>
        <a class="more" style="top:39px" href="#">READ MORE ›</a>
      </div>
      <div class="news-item" style="top:54px">
        <div class="news-photo" role="img" aria-label="Photo of a red ride-on mower cutting grass"></div>
        <div class="news-date">APRIL 22, 2015</div>
        <h5>First quartal 2015 revenue report released</h5>
        <a class="more" style="top:39px" href="#">READ MORE ›</a>
      </div>
      <div style="position:absolute;left:0;top:108px;width:167px;border-top:1px solid #eee;padding-top:6px;text-align:right;font-style:italic;font-size:5.5px;color:#888">Read all news</div>
    </div>

    <div class="abs col-rule" style="left:241px"></div>
    <h3 class="abs col-title" style="left:241px">WHAT CLIENTS SAY</h3>
    <div class="abs quote">
      <p>Best customer support and response time I have evr seen... not to mention a kick ass theme! Great feeling from this pourchase. Thank you Harbor Works!</p>
      <div class="mark"></div>
      <b>DANA WHITFIELD,<br>TRANSPORT &amp; LOGISTICS SOLUTIONS</b>
    </div>
    <span class="abs arrow-btn" style="left:241px;top:1208px;background:#1b2430"><svg width="6" height="8" viewBox="0 0 6 8"><path d="M5 1L2 4l3 3" stroke="#fff" stroke-width="1.4" fill="none"/></svg></span>
    <span class="abs arrow-btn" style="left:389px;top:1208px;background:var(--yellow)"><svg width="6" height="8" viewBox="0 0 6 8"><path d="M1 1l3 3-3 3" stroke="#fff" stroke-width="1.4" fill="none"/></svg></span>

    <div class="abs col-rule" style="left:421px"></div>
    <h3 class="abs col-title" style="left:421px">OUR LOCATIONS</h3>
    <div class="abs map" role="img" aria-label="Map showing service locations marked with red pins"></div>
    <p class="abs" style="left:421px;top:1228px;width:167px;font-size:5.5px;line-height:9.2px;color:#666">Bright Furrow serves over 150 locations across the region, plus numerous partner properties from different areas of the county.</p>
    <a class="abs" style="left:517px;top:1261px;font-family:Roboto,sans-serif;font-weight:700;font-size:5.5px;color:var(--blue)" href="#">VIEW ALL LOCATIONS
      <svg width="5" height="7" viewBox="0 0 10 14" style="vertical-align:-1px;margin-left:2px"><path d="M5 0a5 5 0 015 5c0 4-5 9-5 9S0 9 0 5a5 5 0 015-5z" fill="#1a73c4"/><circle cx="5" cy="5" r="2" fill="#fff"/></svg></a>
  </section>

  <footer class="abs footer">
    <h6 style="left:60px">NEWSLETTER SUBSCRIBE</h6>
    <p class="txt" style="left:60px;top:51px;width:118px">Subscribe to our newsletter and we will inform you about newset projects and promotions.</p>
    <div class="subscribe"><span>Your email address</span><i></i></div>

    <h6 style="left:196px">QUICK LINKS</h6>
    <ul style="left:196px"><li>About us</li><li>Lawn Care Management</li><li>Company News</li><li>Promotions</li><li>Consulting Services</li><li>Privacy Policy</li><li>Track your Request</li></ul>

    <h6 style="left:332px">INDUSTRY SOLUTIONS</h6>
    <ul style="left:332px"><li>Automotive</li><li>Chemicals</li><li>Energy, Oil and Gas</li><li>Food and Beverages</li><li>Retail Goods</li><li>Pharmaceutical</li><li>Consumer Goods</li></ul>

    <h6 style="left:468px">CONTACT US</h6>
    <p class="txt" style="left:468px;top:51px;line-height:11.3px">48 Millbrook Lane,<br>Towson, Maryland</p>
    <p class="abs" style="left:468px;top:76px;font-size:8px;color:#fff">+00 10 555 019 2244</p>
    <p class="txt" style="left:468px;top:92px">hello@brightfurrow.example</p>
    <div class="social" style="left:468px"><span></span><span></span><span></span></div>

    <div class="copyright">BRIGHT FURROW 2018. ALL RIGHTS RESERVED</div>
  </footer>

</div>
</div>
</body>
</html>
```